Need to design a business card with logo

Hellow
we are a company ,
PT REKA LINTAS MANDIRI
looking for design of name card.
what we do is property development and management.
design preferable professional corporate look and feel.
corporate. color, pantone colour 289
information required is
company name " Reka Lintas Mandiri"
person name eg " Peter Hollis"
person title eg "secret agent"
address: 9 kestrel road , jakarta, indonesia
phone : +6221 5906471
mobile : 0813 294 615
email : peter@hollistran.com
website: www.peterhol.com
if you want to include logo in the design you are welcome and appreciated , or you can simply use the company name as the logo.
thanks
corporate , business person , show events, exhibition events ,etc
Business

```html
<!DOCTYPE html>
<html lang="en">
<head>
<meta charset="utf-8">
<title>Reka Lintas Mandiri — Business Card</title>
<link rel="stylesheet" href="https://fonts.googleapis.com/css2?family=Open+Sans:wght@400;600;700&family=Oswald:wght@500&display=swap">
<style>
  :root {
    --page-bg: #e9ebee;
    --navy-deep: #061f45;
    --navy: #0b3a78;
    --navy-mid: #0f4f9c;
    --corporate-blue: #0e4c92;
    --cyan: #1aa3e0;
    --ink: #2a2f36;
    --ink-soft: #6b7380;
    --white: #ffffff;
    --divider: #5a6270;
  }
  * { box-sizing: border-box; margin: 0; padding: 0; }
  html, body {
    width: 1200px;
    height: 3000px;
    overflow: hidden;
    background: var(--page-bg);
    font-family: "Open Sans", Arial, sans-serif;
  }
  .canvas {
    width: 1200px;
    height: 3000px;
    display: flex;
    flex-direction: column;
    align-items: center;
    justify-content: center;
    gap: 200px;
  }
  .card {
    position: relative;
    width: 1040px;
    height: 594px;
    border-radius: 34px;
    overflow: hidden;
    box-shadow: 0 18px 40px rgba(10, 30, 60, 0.18);
  }

  /* Front */
  .card-front {
    background: linear-gradient(160deg, var(--navy-mid) 0%, var(--navy) 45%, var(--navy-deep) 100%);
    color: var(--white);
  }
  .card-front .bands {
    position: absolute;
    inset: 0;
    width: 100%;
    height: 100%;
  }
  .front-brand {
    position: absolute;
    left: 50%;
    top: 50%;
    transform: translate(-50%, -50%);
    display: flex;
    align-items: center;
    gap: 44px;
  }
  .front-brand .brand-dot {
    width: 150px;
    height: 150px;
    border-radius: 50%;
    background: var(--white);
    flex: none;
  }
  .front-brand .brand-name {
    font-weight: 700;
    font-size: 60px;
    letter-spacing: 1px;
    line-height: 1;
    text-transform: uppercase;
  }
  .front-brand .brand-tagline {
    margin-top: 14px;
    font-weight: 400;
    font-size: 30px;
    letter-spacing: 0.5px;
  }

  /* Back */
  .card-back {
    background: var(--white);
  }
  .back-brand {
    position: absolute;
    left: 70px;
    top: 130px;
    width: 340px;
    display: flex;
    flex-direction: column;
    align-items: center;
    gap: 26px;
  }
  .back-brand .brand-dot {
    width: 150px;
    height: 150px;
    border-radius: 50%;
    background: linear-gradient(180deg, var(--cyan) 0%, var(--corporate-blue) 55%, var(--navy-deep) 100%);
  }
  .back-brand .brand-name {
    font-weight: 700;
    font-size: 30px;
    color: var(--corporate-blue);
    text-transform: uppercase;
    letter-spacing: 0.5px;
    white-space: nowrap;
  }
  .divider {
    position: absolute;
    left: 450px;
    top: 70px;
    width: 2px;
    height: 340px;
    background: var(--divider);
  }
  .contact {
    position: absolute;
    left: 490px;
    top: 66px;
    color: var(--ink);
  }
  .contact .person-name {
    font-family: "Oswald", "Arial Narrow", sans-serif;
    font-weight: 500;
    font-size: 44px;
    line-height: 1.1;
    color: var(--navy-deep);
    letter-spacing: 1px;
    text-transform: uppercase;
  }
  .contact .person-title {
    font-size: 22px;
    color: var(--ink-soft);
    margin-bottom: 26px;
  }
  .contact-list { list-style: none; }
  .contact-list li {
    display: flex;
    align-items: center;
    gap: 14px;
    font-size: 24px;
    line-height: 36px;
  }
  .contact-list svg { width: 20px; height: 20px; flex: none; }
  .contact-list .web { color: var(--cyan); }
  .address {
    margin-top: 22px;
    font-size: 24px;
    line-height: 32px;
    color: var(--ink);
  }
  .back-stripes {
    position: absolute;
    left: 0;
    bottom: 0;
    width: 100%;
    height: 150px;
  }
</style>
</head>
<body>
<main class="canvas">

  <section class="card card-front" aria-label="Card front">
    <svg class="bands" viewBox="0 0 1040 594" preserveAspectRatio="none" aria-hidden="true">
      <g fill="#ffffff" fill-opacity="0.04">
        <polygon points="0,120 420,0 560,0 0,170"/>
        <polygon points="0,330 1040,40 1040,110 0,400"/>
        <polygon points="300,594 1040,380 1040,450 500,594"/>
      </g>
      <g fill="#000000" fill-opacity="0.08">
        <polygon points="0,470 1040,170 1040,230 0,530"/>
      </g>
    </svg>
    <div class="front-brand">
      <div class="brand-dot"></div>
      <div>
        <div class="brand-name">Reka Lintas Mandiri</div>
        <div class="brand-tagline">property development and management</div>
      </div>
    </div>
  </section>

  <section class="card card-back" aria-label="Card back">
    <div class="back-brand">
      <div class="brand-dot"></div>
      <div class="brand-name">Reka Lintas Mandiri</div>
    </div>

    <div class="divider"></div>

    <div class="contact">
      <div class="person-name">Peter Hollis</div>
      <div class="person-title">General Manager</div>
      <ul class="contact-list">
        <li>
          <svg viewBox="0 0 20 20" aria-hidden="true"><rect width="20" height="20" rx="4" fill="#0b3a78"/><path d="M6 4.5c.6-.4 1.3-.2 1.6.4l.9 1.8c.2.5.1 1-.3 1.3l-.7.6c.6 1.3 1.6 2.3 2.9 2.9l.6-.7c.3-.4.9-.5 1.3-.3l1.8.9c.6.3.8 1 .4 1.6l-.6.9c-.5.7-1.4 1-2.2.7C8.6 13.5 6.5 11.4 5.4 8.3c-.3-.8 0-1.7.7-2.2z" fill="#fff"/></svg>
          <span>+6221 5906471</span>
        </li>
        <li>
          <svg viewBox="0 0 20 20" aria-hidden="true"><rect width="20" height="20" rx="4" fill="#0b3a78"/><rect x="6.5" y="3.5" width="7" height="13" rx="1.5" fill="#fff"/><rect x="8" y="5.5" width="4" height="7" fill="#0b3a78"/></svg>
          <span>0813 294 615</span>
        </li>
        <li>
          <svg viewBox="0 0 20 20" aria-hidden="true"><rect width="20" height="20" rx="4" fill="#0b3a78"/><rect x="4" y="6" width="12" height="8.5" rx="1" fill="#fff"/><path d="M4.5 6.5 10 11l5.5-4.5" stroke="#0b3a78" stroke-width="1.3" fill="none"/></svg>
          <span>peter@hollistran.com</span>
        </li>
        <li>
          <svg viewBox="0 0 20 20" aria-hidden="true"><rect width="20" height="20" rx="4" fill="#0b3a78"/><circle cx="10" cy="10" r="5.5" stroke="#fff" stroke-width="1.3" fill="none"/><path d="M4.5 10h11M10 4.5c-2.4 3-2.4 8 0 11M10 4.5c2.4 3 2.4 8 0 11" stroke="#fff" stroke-width="1.1" fill="none"/></svg>
          <span class="web">www.peterhol.com</span>
        </li>
      </ul>
      <div class="address">9 kestrel road<br>Jakarta, Indonesia</div>
    </div>

    <svg class="back-stripes" viewBox="0 0 1040 150" preserveAspectRatio="none" aria-hidden="true">
      <polygon points="0,112 1040,40 1040,52 0,124" fill="#1aa3e0"/>
      <polygon points="0,126 1040,54 1040,76 0,148" fill="#0e4c92"/>
      <polygon points="0,138 1040,70 1040,150 0,150" fill="#061f45"/>
    </svg>
  </section>

</main>
</body>
</html>
```